Web site for radio show

I've got a radio show starting on VandorFM and need a web site for it. I am familiar with WordPress, so I'd like to get a design for a WordPress-based web site for the show.

I'm also posting a logo project to be done at the same time.

The best radio show web site I've seen is the Lumen Tuesday site (www.lumentuesday.example). That's a good model but I don't want to start with that much complexity and content. The initial site that I'd like you to design would have the following parts:
- Upcoming shows
- Past shows (including links to authors, their web sites, and their books)
- Chirply feed
- Blog
- About
- ...and anything else you think would be necessary

For colors, I'd like it to be consistent with my personal web site: www.haldanecraftworks.example

Target Market(s)

The target market for this show is mid- to upper-level managers

Industry/Entity Type

Radio

Requirements
Must have
• The project has to proceed in (at least) two stages: a first rough layout, and a second finished design. Whether you want a third stage in between with look and feel options is up to you.

```html
<!DOCTYPE html>
<html lang="en">
<head>
<meta charset="utf-8">
<title>Haldane Show</title>
<link href="https://fonts.googleapis.com/css2?family=Source+Sans+3:ital,wght@0,300;0,400;0,600;0,700;1,400&display=swap" rel="stylesheet">
<style>
:root{
  --red:#c00a0a;
  --red-dark:#a80000;
  --ink:#222;
  --grey-text:#777;
  --grey-nav:#7a7a7a;
  --frame:#cfcfcf;
  --band:#d9d9d9;
  --social:#bdbdbd;
  --chirp:#1ea1e6;
  --brand-blue:#1a5fa8;
}
*{box-sizing:border-box;margin:0;padding:0}
html,body{width:1200px;height:1061px;overflow:hidden;background:#fff}
body{position:relative;font-family:"Source Sans 3",Arial,sans-serif;color:var(--ink)}
.abs{position:absolute}
.top-strip{left:0;top:0;width:1200px;height:6px;background:var(--band)}
.brand{left:128px;top:32px;font-size:25px;font-weight:700;color:var(--red);letter-spacing:1px}
.social{top:13px;width:29px;height:29px;border-radius:50%;background:var(--social)}
.nav{right:147px;top:64px;display:flex;gap:15px;font-size:15.5px;font-weight:600;color:var(--grey-nav)}
.frame{border:1px solid var(--frame);background:#fff}
.photo{background:linear-gradient(135deg,#8a8079,#c9c2bb)}
.hero-photo{left:120px;top:108px;width:607px;height:338px;background:linear-gradient(90deg,#c9c3bf 0%,#e9e7e6 40%,#f6f6f6 60%,#f1f1f1 100%)}
.hero-title{left:438px;top:184px;font-size:38px;font-weight:600;color:#555;letter-spacing:-.5px}
.hero-title span{color:var(--red)}
.hero-text{left:444px;top:233px;width:240px;font-size:12.5px;line-height:18px;color:#222}
.btn{background:var(--red);color:#fff;font-weight:600;display:flex;align-items:center;justify-content:center}
.play-btn{left:444px;top:298px;width:88px;height:30px;border-radius:4px;font-size:17px}
.events{left:120px;top:398px;width:607px;height:48px;background:rgba(70,70,70,.9);color:#fff}
.events h3{position:absolute;left:15px;top:6px;font-size:28px;font-weight:600}
.events p{position:absolute;left:266px;top:6px;width:275px;font-size:12.5px;line-height:18px}
.arrow{top:12px;width:20px;height:20px;background:var(--red)}
.section-title{font-size:27px;font-weight:600;color:var(--red)}
.past-item .thumb{position:absolute;left:0;top:0;width:98px;height:76px}
.past-item p{position:absolute;left:108px;top:-4px;width:212px;font-size:12.5px;line-height:18px;text-align:justify}
.past-item a{position:absolute;right:-4px;top:58px;font-size:13px;color:var(--red);text-decoration:none}
.chirp-tab{left:1159px;top:207px;width:62px;height:60px;border-radius:50%;background:var(--chirp);border:2px solid #fff;box-shadow:0 0 2px rgba(0,0,0,.3)}
.body-text{font-size:12.5px;line-height:18px;text-align:justify}
.blog-band{left:391px;top:717px;width:307px;height:49px;background:#000;color:#fff;font-size:22px;padding:10px 12px}
.rule{left:109px;top:807px;width:983px;height:1px;background:#d0d0d0}
.foot-title{top:824px;font-size:20px;font-weight:300;color:#222}
.foot-links{list-style:none;font-size:15px;font-weight:300;color:var(--grey-text);line-height:24px}
.email-field{left:404px;top:858px;width:242px;height:35px;border:1px solid #ccc;border-radius:18px;padding:8px 16px;font-size:12.5px;font-style:italic;color:#555}
.note{left:410px;top:904px;width:237px;font-size:13px;line-height:17px;font-style:italic;color:#555;text-align:justify}
.submit{left:403px;top:962px;width:100px;height:31px;border-radius:16px;font-size:17px;font-weight:400}
.contact{left:691px;top:854px;font-size:15px;font-weight:300;color:#333;line-height:24px}
.contact li{list-style:none;position:relative;padding-left:20px}
.contact svg{position:absolute;left:0;top:5px}
.partner{left:888px;top:870px;font-size:30px;font-weight:700;color:var(--brand-blue)}
.footer{left:0;top:1010px;width:1200px;height:51px;background:var(--band);font-size:13px;color:#555}
.footer span{position:absolute;top:18px}
</style>
</head>
<body>
<div class="abs top-strip"></div>
<div class="abs brand">HALDANE SHOW</div>
<div class="abs social" style="left:885px"></div>
<div class="abs social" style="left:920px"></div>
<div class="abs social" style="left:955px"></div>
<div class="abs social" style="left:990px"></div>
<div class="abs social" style="left:1025px"></div>
<nav class="abs nav"><span>Home</span><span>About Us</span><span>Upcoming shows</span><span>Past shows</span><span>Chirply feed</span><span>Blog</span><span>Contact Us</span></nav>

<section>
  <div class="abs frame" style="left:109px;top:98px;width:628px;height:358px"></div>
  <div class="abs hero-photo" role="img" aria-label="Woman with flying hair listening to music on headphones"></div>
  <h1 class="abs hero-title"><span>Today</span> New Show</h1>
  <p class="abs hero-text">Lorem ipsum dolor sit amet, consectetur adipisicing elit, sed do eiusmod tempor incididunt ut labore et dolore magna</p>
  <div class="abs btn play-btn">Play Now</div>
  <div class="abs events">
    <h3>Up comming Events :</h3>
    <p>Lorem ipsum dolor sit amet, consectetur adipisicing elit, sed do eiusmod tempor</p>
    <svg class="abs arrow" style="left:555px" viewBox="0 0 20 20"><path d="M13 5 7 10l6 5z" fill="#fff"/></svg>
    <svg class="abs arrow" style="left:578px" viewBox="0 0 20 20"><path d="M7 5l6 5-6 5z" fill="#fff"/></svg>
  </div>
</section>

<aside>
  <div class="abs frame" style="left:746px;top:98px;width:346px;height:358px"></div>
  <h2 class="abs section-title" style="left:776px;top:114px">Past Shows</h2>
  <div class="abs past-item" style="left:764px;top:160px;width:318px">
    <div class="thumb photo" role="img" aria-label="Studio microphone with a football"></div>
    <p>Lorem ipsum dolor sit amet, consectetur adipisicing elit, sed do eiusmod tempor incididunt ut labore et dolore magna</p>
    <a href="#">Read more</a>
  </div>
  <div class="abs past-item" style="left:764px;top:260px;width:318px">
    <div class="thumb" style="background:linear-gradient(135deg,#eee,#b98a6a)" role="img" aria-label="Girl covering her ears"></div>
    <p>Lorem ipsum dolor sit amet, consectetur adipisicing elit, sed do eiusmod tempor incididunt ut labore et dolore magna</p>
    <a href="#">Read more</a>
  </div>
  <div class="abs past-item" style="left:764px;top:361px;width:318px">
    <div class="thumb photo" role="img" aria-label="Radio mixing desk with microphone"></div>
    <p>Lorem ipsum dolor sit amet, consectetur adipisicing elit, sed do eiusmod tempor incididunt ut labore et dolore magna</p>
    <a href="#">Read more</a>
  </div>
</aside>
<div class="abs chirp-tab"></div>

<section>
  <h2 class="abs section-title" style="left:117px;top:468px">About Us</h2>
  <div class="abs photo" style="left:112px;top:509px;width:264px;height:142px" role="img" aria-label="Radio host at a studio microphone"></div>
  <p class="abs body-text" style="left:117px;top:663px;width:235px">Lorem ipsum dolor sit amet, consectetur adipisicing elit, sed do eiusmod tempor incididunt ut labore et dolore magna Sed ut perspiciatis unde omnis iste natus error sit voluptatem accusantium doloremque laudantium, totam</p>

  <h2 class="abs section-title" style="left:393px;top:468px">Blog</h2>
  <div class="abs" style="left:391px;top:509px;width:307px;height:208px;background:linear-gradient(135deg,#6c6f75,#e8e6e4)" role="img" aria-label="Camera operator filming an interview"></div>
  <div class="abs blog-band">Blog Title Goes Here</div>

  <h2 class="abs section-title" style="left:719px;top:466px">Video</h2>
  <div class="abs" style="left:709px;top:509px;width:369px;height:257px;background:linear-gradient(135deg,#4a3f38,#8a6f5e 50%,#5a4a5e)" role="img" aria-label="Group of friends singing into microphones"></div>
  <svg class="abs" style="left:868px;top:613px" width="54" height="54" viewBox="0 0 54 54"><circle cx="27" cy="27" r="25" fill="rgba(20,20,20,.85)" stroke="#bbb" stroke-width="1.5"/><path d="M21 16l16 11-16 11z" fill="#fff"/></svg>
</section>

<div class="abs rule"></div>
<footer>
  <h4 class="abs foot-title" style="left:129px">LINKS</h4>
  <ul class="abs foot-links" style="left:130px;top:857px"><li>Home</li><li>About Us</li><li>Upcoming shows</li><li>Past shows</li></ul>
  <ul class="abs foot-links" style="left:297px;top:860px"><li>Chirply feed</li><li>Blog</li><li>Contact Us</li></ul>

  <h4 class="abs foot-title" style="left:411px">NEWSLETTER SIGN UP</h4>
  <div class="abs email-field">Enter your email id</div>
  <p class="abs note">We have a lot to say. But we promise you'll find it valuable. We don't spam and we won't sell your data. Give us a try!</p>
  <div class="abs btn submit">Submit</div>

  <h4 class="abs foot-title" style="left:696px">CONTACT US</h4>
  <ul class="abs contact">
    <li><svg width="13" height="12" viewBox="0 0 13 12"><path d="M6.5 0 0 6h2v6h3.5V8h2v4H11V6h2z" fill="#555"/></svg>Lorium ipsum</li>
    <li>XYZ Postfach 90</li>
    <li>9400 Brenwil SG</li>
    <li><svg width="13" height="13" viewBox="0 0 13 13"><path d="M2.5 0 5 3 3.5 4.5c.8 2 2.5 3.7 4.5 4.5L9.5 7.5 13 10l-1.5 2.5C6 12 1 7 .5 1.5z" fill="#555"/></svg>Tel: +41 41 555 01 90</li>
    <li><svg width="11" height="13" viewBox="0 0 11 13"><path d="M0 0h7l4 4v9H0z" fill="#555"/></svg>email : info@haldaneshow.example</li>
  </ul>
  <div class="abs partner">VandorFM</div>

  <div class="abs footer"><span style="left:129px">© 2014.www.companyname.example</span><span style="left:1033px">M1</span></div>
</footer>
</body>
</html>
```